Design my Display Ad! Product for Muscle Cramps -- Need Your Talent!

I need the PSD of a square display ad to be the design concept for other ad formats. The product is for leg and muscle cramps. The ad needs to encourage clicks, not simply impressions. Image should contain legs.

Visit www.legsoothewell.com for a better idea of the product.

Target Market(s)

People age 55+ with leg cramps

Industry/Entity Type

Health And Wellness

Font styles to use
Sans Serif

Colors

Designer to choose colors to be used in the design.

Requirements
Must have
• One version with the text:
• The Real Cause of Leg Cramps
• Discover the Secret
• The other version with the text:
• Leg Cramps at Night
• Discover the Real Cause
• An image focused on legs.
• Attractive presentation -- this is a premium organic brand.
• Visit www.legsoothewell.com for a better understanding of the product

```html
<!DOCTYPE html>
<html lang="en">
<head>
<meta charset="utf-8">
<title>LegSootheWell Display Ads</title>
<link rel="stylesheet" href="https://fonts.googleapis.com/css2?family=Oswald:wght@400;500&display=swap">
<style>
  :root {
    --stage: #d6d6d6;
    --sky-light: #f4f8fb;
    --sky-mid: #bfdcef;
    --sky-deep: #58aedc;
    --leg-blue: #4aa3d6;
    --leg-pale: #a9d2ec;
    --pain-red: #d8183a;
    --brand-blue: #1f8fd6;
    --ink: #1a1512;
    --cta-red: #e8143c;
    --white: #ffffff;
  }
  * { margin: 0; padding: 0; box-sizing: border-box; }
  html, body {
    width: 1200px;
    height: 1200px;
    overflow: hidden;
    background: var(--stage);
  }
  .ad {
    position: absolute;
    top: 315px;
    width: 525px;
    height: 525px;
    overflow: hidden;
    font-family: "Oswald", sans-serif;
  }
  .ad--cause { left: 48px; }
  .ad--night { left: 615px; }
  .ad__backdrop {
    position: absolute;
    inset: 0;
  }
  .ad--cause .ad__backdrop {
    background: linear-gradient(100deg, var(--sky-mid) 0%, var(--sky-light) 55%, var(--sky-mid) 100%);
  }
  .ad--night .ad__backdrop {
    background: linear-gradient(80deg, var(--sky-mid) 0%, var(--sky-light) 45%, var(--sky-light) 70%, var(--sky-mid) 100%);
  }
  .leg-photo {
    position: absolute;
    top: 0;
    left: 0;
    width: 215px;
    height: 100%;
    -webkit-mask-image: linear-gradient(90deg, #000 70%, transparent 100%);
    mask-image: linear-gradient(90deg, #000 70%, transparent 100%);
  }
  .ad--cause .leg-photo {
    background:
      radial-gradient(ellipse 55px 80px at 88px 235px, var(--pain-red) 0%, rgba(216,24,58,0.45) 45%, rgba(216,24,58,0) 100%),
      linear-gradient(180deg, var(--leg-blue) 0%, var(--leg-pale) 60%, var(--sky-mid) 100%);
  }
  .ad--night .leg-photo {
    background:
      radial-gradient(ellipse 60px 75px at 95px 360px, var(--pain-red) 0%, rgba(216,24,58,0.45) 45%, rgba(216,24,58,0) 100%),
      linear-gradient(180deg, var(--leg-blue) 0%, var(--leg-pale) 45%, var(--sky-light) 100%);
  }
  .ad__content {
    position: absolute;
    left: 175px;
    top: 0;
    width: 340px;
    height: 100%;
    text-align: center;
  }
  .brand {
    position: absolute;
    top: 62px;
    left: 0;
    width: 100%;
    font-size: 27px;
    font-weight: 500;
    letter-spacing: 1.5px;
    color: var(--brand-blue);
    text-transform: uppercase;
  }
  .headline {
    position: absolute;
    left: 0;
    width: 100%;
    font-weight: 400;
    font-size: 74px;
    line-height: 72px;
    color: var(--ink);
    letter-spacing: -1.5px;
  }
  .ad--cause .headline { top: 145px; }
  .ad--night .headline { top: 145px; line-height: 70px; }
  .cta {
    position: absolute;
    top: 408px;
    height: 62px;
    border-radius: 31px;
    background: var(--cta-red);
    color: var(--white);
    font-size: 25px;
    font-weight: 500;
    line-height: 62px;
    text-transform: uppercase;
    text-align: center;
    letter-spacing: 0.3px;
  }
  .ad--cause .cta { left: 20px; width: 291px; }
  .ad--night .cta { left: -7px; width: 342px; }
</style>
</head>
<body>
  <section class="ad ad--cause">
    <div class="ad__backdrop"></div>
    <div class="leg-photo" role="img" aria-label="Person gripping a cramping calf while walking outdoors, pain area glowing red"></div>
    <div class="ad__content">
      <div class="brand">LegSootheWell</div>
      <h1 class="headline">The Real<br>Cause of<br>Leg Cramps</h1>
      <div class="cta">Discover the Secret</div>
    </div>
  </section>

  <section class="ad ad--night">
    <div class="ad__backdrop"></div>
    <div class="leg-photo" role="img" aria-label="Hands holding a bare calf with the cramping muscle glowing red"></div>
    <div class="ad__content">
      <div class="brand">LegSootheWell</div>
      <h1 class="headline">Leg<br>Cramps<br>at Night</h1>
      <div class="cta">Discover the Real Cause</div>
    </div>
  </section>
</body>
</html>
```